5-star Hotel Web Design Project

I need a custom website design for a 5-star hotel. For full details please look at the attached ZIP archive.

The design should be in layers in Photoshop/Illustrator/InDesign format with all the icons/shapes/maps/graphic assets in vector format (svg, ai, eps) as much as possible.

I prefer white, simple but elegant websites. Please consider the performance/coding experience. We're not making something to show off our design skills on a design contest with fancy parallax effects and confusing animations. We're trying to create usable, functional and clean UI with good UX.

I would like to receive a few option for the color scheme to choose from.

The website will be custom coded, i.e. I'm not using WordPress.

NOTE: Don't bother to submit the generic WordPress style templates. We're looking for something custom made with attention to details. That's why the price is not guaranteed, but don't be mistaken, I'm a long time buyer here on SketchHive and all my projects are paid in full.

Low design quality

Europe

Hotel

5+ page

```html
<!DOCTYPE html>
<html lang="en">
<head>
<meta charset="utf-8">
<title>Amberview Resort – Home</title>
<link rel="stylesheet" href="https://fonts.googleapis.com/css2?family=Cinzel:wght@400;500&family=Poppins:wght@400;500&display=swap">
<style>
  :root {
    --crimson: #a5123f;
    --crimson-dark: #8d0f36;
    --gold: #d2aa63;
    --night: #1f1c1e;
    --pool: #1f6f86;
    --white: #ffffff;
    --text-light: #f2ecea;
  }
  * { margin: 0; padding: 0; box-sizing: border-box; }
  html, body { width: 1200px; height: 800px; overflow: hidden; background: var(--white); }
  body { font-family: "Poppins", sans-serif; color: var(--text-light); }

  .page { position: relative; width: 1200px; height: 800px; overflow: hidden; }

  .hero-photo {
    position: absolute; inset: 0;
    background:
      linear-gradient(180deg, rgba(25,22,24,0.92) 0%, rgba(25,22,24,0.55) 18%, rgba(40,36,38,0.35) 45%, rgba(20,18,20,0.7) 100%),
      linear-gradient(180deg, #3a3434 0%, #4a4442 40%, #2c4f5c 62%, var(--pool) 70%, #2a2624 80%, #1a1718 100%);
  }

  .top-bar {
    position: absolute; top: 0; left: 0; right: 0; height: 38px;
    background: var(--crimson);
    display: flex; align-items: center; justify-content: flex-end;
    padding-right: 140px; gap: 26px;
    font-size: 12px; color: var(--white);
  }
  .top-bar .contact-btn {
    border: 1px solid var(--white); border-radius: 6px;
    padding: 2px 14px; color: var(--white); text-decoration: none;
  }
  .top-bar .language { display: flex; align-items: center; gap: 5px; }

  .site-header {
    position: absolute; top: 38px; left: 0; right: 0; height: 120px;
    display: flex; align-items: center; justify-content: space-between;
    padding: 0 140px 0 150px;
  }
  .brand {
    display: flex; flex-direction: column; align-items: center; gap: 4px;
    font-family: "Cinzel", serif; color: var(--white);
  }
  .brand-name { font-size: 22px; letter-spacing: 1px; }
  .brand-stars { font-size: 10px; letter-spacing: 3px; color: var(--white); }
  .main-nav { display: flex; gap: 52px; font-size: 13px; }
  .main-nav a { color: var(--white); text-decoration: none; }

  .hero-content {
    position: absolute; top: 290px; left: 0; right: 0;
    text-align: center;
  }
  .hero-title {
    font-family: "Cinzel", serif; font-weight: 400;
    font-size: 62px; line-height: 1.18; letter-spacing: 1px;
  }
  .hero-title .line-gold { color: var(--gold); display: block; }
  .hero-title .line-crimson { color: var(--crimson); display: block; }

  .booking-bar {
    margin-top: 20px; display: inline-flex; gap: 6px;
  }
  .booking-bar a {
    display: inline-block; padding: 8px 26px; border-radius: 6px 6px 0 0;
    font-size: 14px; color: var(--white); text-decoration: none;
    background: var(--crimson);
  }
  .booking-bar a.check-availability { background: var(--gold); padding: 8px 34px; }

  .slider-dots {
    position: absolute; top: 662px; left: 0; right: 0;
    display: flex; justify-content: center; gap: 12px;
  }
  .slider-dots span { width: 46px; height: 3px; background: rgba(255,255,255,0.35); }
  .slider-dots span.active { background: var(--white); }

  .hero-curve { position: absolute; left: 0; bottom: 0; width: 1200px; height: 130px; }
</style>
</head>
<body>
<div class="page">
  <div class="hero-photo" role="img" aria-label="Photograph of the resort building at night with an illuminated swimming pool in front"></div>

  <div class="top-bar">
    <span class="phone">+0 555 014 2260</span>
    <a class="contact-btn" href="#">Contact us</a>
    <span class="language">
      <svg width="8" height="6" viewBox="0 0 8 6"><path d="M1 1l3 3 3-3" fill="none" stroke="#fff" stroke-width="1.2"/></svg>
      English
    </span>
  </div>

  <header class="site-header">
    <div class="brand">
      <span class="brand-stars">★★★★★</span>
      <span class="brand-name">Amberview Resort</span>
    </div>
    <nav class="main-nav">
      <a href="#">Amberview Resort</a>
      <a href="#">Book direct</a>
      <a href="#">Special Offers</a>
      <a href="#">Location</a>
    </nav>
  </header>

  <section class="hero-content">
    <h1 class="hero-title">
      <span class="line-gold">Book now with</span>
      <span class="line-crimson">20% discount</span>
    </h1>
    <div class="booking-bar">
      <a href="#" class="check-in">Check In</a>
      <a href="#" class="check-availability">Check Availability</a>
      <a href="#" class="check-out">Check Out</a>
    </div>
  </section>

  <div class="slider-dots">
    <span class="active"></span><span></span><span></span><span></span>
  </div>

  <svg class="hero-curve" viewBox="0 0 1200 130" preserveAspectRatio="none">
    <path d="M0 40 C 300 150, 800 130, 1200 0 L1200 130 L0 130 Z" fill="#ffffff"/>
  </svg>
</div>
</body>
</html>
```